Moravel Stenwick Inc needs a business card design

Looking for a unique, classy and sharp business card design.

Contact Information for Business Card

Moravel Stenwick Inc.
Marisa Ortega Bellido BScOT(c)
Occupational Therapist
(780) 555-0142
moravelstenwick@postlynx.net

```html
<!DOCTYPE html>
<html lang="en">
<head>
<meta charset="utf-8">
<title>Moravel Stenwick Inc. – Business Card</title>
<link rel="stylesheet" href="https://fonts.googleapis.com/css2?family=Montserrat:wght@400;500;700&display=swap">
<style>
  :root {
    --page-bg: #2b2d31;
    --card-white: #f3f3f2;
    --sky-blue: #23a8e1;
    --name-blue: #1c86cf;
    --leaf-green: #8dc63f;
    --brand-purple: #7b2d8e;
    --ink: #2a2a2a;
  }
  * { margin: 0; padding: 0; box-sizing: border-box; }
  html, body {
    width: 1200px;
    height: 1000px;
    overflow: hidden;
    background: var(--page-bg);
    font-family: "Montserrat", Arial, sans-serif;
  }
  .stage {
    width: 1200px;
    height: 1000px;
    display: flex;
    align-items: center;
    justify-content: center;
  }
  .business-card {
    position: relative;
    width: 480px;
    height: 820px;
    border-radius: 34px;
    overflow: hidden;
    background: var(--card-white);
  }
  .card-waves {
    position: absolute;
    inset: 0;
    width: 100%;
    height: 100%;
  }
  .wave-blue { fill: var(--sky-blue); }
  .wave-green { fill: var(--leaf-green); }
  .brand {
    position: absolute;
    top: 78px;
    left: 0;
    right: 0;
    display: flex;
    align-items: center;
    justify-content: center;
    gap: 14px;
  }
  .brand-dot {
    width: 46px;
    height: 46px;
    border-radius: 50%;
    background: var(--leaf-green);
  }
  .brand-name {
    font-weight: 700;
    font-size: 30px;
    line-height: 1.05;
    color: var(--brand-purple);
  }
  .person {
    position: absolute;
    top: 250px;
    left: 44px;
  }
  .person-name {
    font-weight: 700;
    font-size: 23px;
    color: var(--name-blue);
    letter-spacing: -0.2px;
  }
  .person-credential {
    font-weight: 500;
    font-size: 18px;
    color: var(--ink);
  }
  .person-title {
    margin-top: 4px;
    font-size: 16px;
    color: var(--ink);
  }
  .contact {
    position: absolute;
    top: 340px;
    left: 44px;
    list-style: none;
  }
  .contact-item {
    display: flex;
    align-items: center;
    gap: 10px;
    font-size: 16px;
    color: var(--ink);
    margin-bottom: 8px;
  }
  .contact-icon {
    width: 18px;
    height: 18px;
    flex: none;
  }
  .contact-icon circle { fill: var(--name-blue); }
  .contact-icon path { fill: none; stroke: #fff; stroke-width: 1.6; stroke-linecap: round; stroke-linejoin: round; }
</style>
</head>
<body>
<main class="stage">
  <article class="business-card">
    <svg class="card-waves" viewBox="0 0 480 820" aria-hidden="true">
      <path class="wave-green" d="M250 468 Q390 420 480 300 L480 332 Q390 440 250 468 Z"/>
      <path class="wave-blue" d="M0 500 Q330 500 480 340 L480 820 L0 820 Z"/>
    </svg>

    <header class="brand">
      <span class="brand-dot"></span>
      <span class="brand-name">Moravel<br>Stenwick Inc.</span>
    </header>

    <section class="person">
      <h1 class="person-name">Marisa Ortega Bellido <span class="person-credential">BScOT(c)</span></h1>
      <p class="person-title">Occupational Therapist</p>
    </section>

    <ul class="contact">
      <li class="contact-item">
        <svg class="contact-icon" viewBox="0 0 18 18" aria-hidden="true">
          <circle cx="9" cy="9" r="9"/>
          <path d="M6 5 L7.5 5 L8.2 7 L7.2 7.8 Q8 9.8 10.2 10.8 L11 9.8 L13 10.5 L13 12 Q9 12.5 6.5 9.5 Q5.5 7.5 6 5 Z"/>
        </svg>
        <span>(780) 555-0142</span>
      </li>
      <li class="contact-item">
        <svg class="contact-icon" viewBox="0 0 18 18" aria-hidden="true">
          <circle cx="9" cy="9" r="9"/>
          <path d="M4.5 6 H13.5 V12.5 H4.5 Z M4.5 6 L9 9.8 L13.5 6"/>
        </svg>
        <span>moravelstenwick@postlynx.net</span>
      </li>
    </ul>
  </article>
</main>
</body>
</html>
```